Dental Co needs single page print ad

Dental company needs a 1 page ad for trade magazines.
I am uploading an example of what we want (words). We need you to make it look great. It can include people or not.
The uploaded ad isn't there to be copied, just to kind of frame what we are thinking. We are open to any design
One page ad
Size 1)

Trim Size - 8 x 10.5
Bleed Size - 8.25 x 10.75
Live Area - 7 x 10

Size 2)

Trim - 8 x 10.875
Bleed - 8.25 x 11.125
Live Area - 7 x 9.875

BRIX Brand Hex #'s

Orange - ff6319
Teal - 56b1bf
Lt. Teal - aed9da
Blue: #38394B

Target Market(s)

Dentists

Requirements
Must have
• BRIX Logo, pic of the sensor (called VANT)
Use the brand hex colors:
Orange - ff6319
Teal - 56b1bf
Lt. Teal - aed9da
Blue: #38394B

```html
<!DOCTYPE html>
<html lang="en">
<head>
<meta charset="utf-8">
<title>VANT Sensor Subscription – Print Ad Sizes</title>
<link rel="stylesheet" href="https://fonts.googleapis.com/css2?family=Montserrat:wght@300;400;500;600;700;800;900&family=Oswald:wght@600&family=Great+Vibes&display=swap">
<style>
  :root{
    --orange:#ff6319;
    --navy:#2d3180;
    --ink:#26295f;
    --white:#ffffff;
    --photo-light:#f4f4f4;
    --photo-mid:#d9d9d9;
    --photo-dark:#a9a9a9;
    --board-top:#2f2f2f;
    --board-bottom:#8a8a8a;
    --sans:'Montserrat', Arial, sans-serif;
    --condensed:'Oswald', 'Arial Narrow', sans-serif;
    --script:'Great Vibes', cursive;
  }
  *{box-sizing:border-box;margin:0;padding:0}
  html,body{width:1200px;height:864px;overflow:hidden}
  body{
    position:relative;
    background:linear-gradient(180deg,var(--board-top) 0%,#5a5a5a 55%,var(--board-bottom) 100%);
    font-family:var(--sans);
  }

  /* ---------- Ad frame ---------- */
  .ad{
    position:absolute;width:467px;background:var(--white);overflow:hidden;
    box-shadow:0 12px 28px rgba(0,0,0,.45);
  }
  .ad--size1{left:86px;top:106px;height:609px;
    --price-top:341px;--sensor-top:404px;--sensor-h:119px;--list-top:416px;--band-top:535px;--web-top:569px}
  .ad--size2{left:647px;top:85px;height:631px;
    --price-top:349px;--sensor-top:415px;--sensor-h:111px;--list-top:428px;--band-top:548px;--web-top:585px}

  .hero-photo{
    position:absolute;left:0;top:0;width:467px;height:262px;
    background:linear-gradient(100deg,var(--white) 0%,var(--photo-light) 40%,var(--photo-mid) 75%,var(--photo-dark) 100%);
  }
  .ad-shapes{position:absolute;inset:0;width:100%;height:100%}

  .headline{
    position:absolute;left:38px;top:40px;
    font-weight:400;font-size:26px;line-height:32px;color:var(--navy);letter-spacing:.3px;
  }
  .headline__accent{color:var(--orange);display:block}
  .headline__lead{display:block}
  .headline__aside{
    position:absolute;left:38px;top:180px;
    font-family:var(--script);font-size:25px;color:var(--navy);
  }

  .product-name{
    position:absolute;left:34px;top:246px;
    font-weight:900;font-size:58px;line-height:1;color:var(--navy);letter-spacing:-1px;
  }
  .tagline{
    position:absolute;right:21px;top:270px;
    font-weight:600;font-size:11.5px;color:var(--navy);
  }
  .social{position:absolute;right:20px;top:305px;display:flex;gap:7px}
  .social__dot{width:20px;height:20px;border:1.6px solid var(--white);border-radius:50%}

  /* ---------- Pricing ---------- */
  .price{
    position:absolute;top:var(--price-top);height:47px;display:flex;align-items:center;
    background:var(--white);box-shadow:0 6px 8px rgba(0,0,0,.25);
  }
  .price--fee{left:21px;width:215px}
  .price--monthly{left:244px;width:201px}
  .price__amount{
    height:100%;display:flex;align-items:center;padding-left:11px;
    background:var(--navy);color:var(--white);
    font-family:var(--condensed);font-weight:600;font-size:27px;
    clip-path:polygon(0 0,88% 0,100% 100%,0 100%);
  }
  .price--fee .price__amount{width:100px}
  .price--monthly .price__amount{width:117px}
  .price__note{
    padding-left:7px;font-weight:500;font-size:13.5px;line-height:16px;color:var(--ink);letter-spacing:.4px;
  }

  .sensor-photo{
    position:absolute;left:14px;top:var(--sensor-top);width:172px;height:var(--sensor-h);
    border-radius:18px;background:linear-gradient(160deg,#3c3f6e 0%,#5d618f 60%,#2a2c55 100%);
  }

  .benefits{position:absolute;left:208px;top:var(--list-top);list-style:none}
  .benefits__item{
    display:flex;align-items:center;gap:6px;height:19px;
    font-size:11.3px;font-weight:400;color:var(--white);white-space:nowrap;
  }
  .benefits__item svg{width:9px;height:9px;flex:none}

  /* ---------- Footer ---------- */
  .phone{
    position:absolute;left:30px;top:calc(var(--band-top) + 2px);
    display:flex;align-items:center;gap:7px;
    font-weight:700;font-size:22px;color:var(--white);letter-spacing:.6px;
  }
  .phone svg{width:22px;height:22px}
  .website{
    position:absolute;left:30px;top:var(--web-top);
    display:flex;align-items:center;gap:5px;
    font-weight:500;font-size:14.5px;color:var(--white);letter-spacing:1.2px;
  }
  .website svg{width:12px;height:12px}
  .company-name{
    position:absolute;right:48px;top:calc(var(--band-top) - 4px);
    font-weight:800;font-size:30px;line-height:27px;color:var(--navy);text-align:center;
  }
  .company-name span{display:block;font-size:17px;letter-spacing:1.5px}

  .size-label{
    position:absolute;top:770px;
    font-weight:700;font-size:31px;color:var(--white);
  }
  .size-label--1{left:160px}
  .size-label--2{left:710px}
</style>
</head>
<body>

<!-- Size 1 -->
<section class="ad ad--size1">
  <div class="hero-photo" role="img" aria-label="Black-and-white photo of a model with orange lips holding the VANT sensor beneath her chin"></div>
  <svg class="ad-shapes" viewBox="0 0 467 609" aria-hidden="true">
    <polygon fill="#ff6319" points="0,320 245,320 272,294 467,294 467,518 300,518 240,602 0,602"/>
    <path d="M198 229 L230 260" stroke="#2d3180" stroke-width="4" fill="none"/>
    <polygon fill="#2d3180" points="0,535 277,535 258,565 0,565"/>
  </svg>
  <h1 class="headline"><span class="headline__lead">A subscription</span><span class="headline__lead">option for</span><span class="headline__accent">intra-oral sensors</span><span class="headline__accent">is dumb.</span></h1>
  <p class="headline__aside">(until you do the math).</p>
  <div class="product-name">VANT</div>
  <p class="tagline">11 Million X-rays and Counting</p>
  <div class="social"><span class="social__dot"></span><span class="social__dot"></span><span class="social__dot"></span></div>
  <div class="price price--fee"><span class="price__amount">$1,999</span><span class="price__note">ONE-TIME<br>SIGN UP FEE</span></div>
  <div class="price price--monthly"><span class="price__amount">$139/mo</span><span class="price__note">CANCEL<br>ANYTIME</span></div>
  <div class="sensor-photo" role="img" aria-label="Product photo of the VANT intra-oral sensor with cable"></div>
  <ul class="benefits">
    <li class="benefits__item"><svg viewBox="0 0 10 10"><circle cx="5" cy="5" r="4.3" fill="none" stroke="#fff" stroke-width="1"/><path d="M3 5.2 L4.5 6.6 L7 3.8" fill="none" stroke="#fff" stroke-width="1"/></svg>Lifetime $0 deductible warranty</li>
    <li class="benefits__item"><svg viewBox="0 0 10 10"><circle cx="5" cy="5" r="4.3" fill="none" stroke="#fff" stroke-width="1"/><path d="M3 5.2 L4.5 6.6 L7 3.8" fill="none" stroke="#fff" stroke-width="1"/></svg>Unlimited support &amp; upgrades</li>
    <li class="benefits__item"><svg viewBox="0 0 10 10"><circle cx="5" cy="5" r="4.3" fill="none" stroke="#fff" stroke-width="1"/><path d="M3 5.2 L4.5 6.6 L7 3.8" fill="none" stroke="#fff" stroke-width="1"/></svg>Direct integration w/all major software</li>
    <li class="benefits__item"><svg viewBox="0 0 10 10"><circle cx="5" cy="5" r="4.3" fill="none" stroke="#fff" stroke-width="1"/><path d="M3 5.2 L4.5 6.6 L7 3.8" fill="none" stroke="#fff" stroke-width="1"/></svg>Affordable enough for every op</li>
    <li class="benefits__item"><svg viewBox="0 0 10 10"><circle cx="5" cy="5" r="4.3" fill="none" stroke="#fff" stroke-width="1"/><path d="M3 5.2 L4.5 6.6 L7 3.8" fill="none" stroke="#fff" stroke-width="1"/></svg>Preserve your capital</li>
  </ul>
  <p class="phone"><svg viewBox="0 0 24 24"><circle cx="12" cy="12" r="10.5" fill="none" stroke="#fff" stroke-width="1.8"/><path d="M8.3 6.5c.6-.4 1.3-.3 1.6.3l1 1.9c.3.5.1 1.1-.3 1.4l-.7.5c.5 1.4 1.5 2.6 2.9 3.3l.6-.6c.4-.4 1-.5 1.5-.2l1.8 1.1c.5.3.7 1 .3 1.5-.9 1.3-2.2 1.7-3.6 1.1-3-1.3-5.1-3.7-6-6.7-.4-1.4.1-2.8.9-3.6z" fill="#fff"/></svg>(555) 010-BRIX</p>
  <p class="website"><svg viewBox="0 0 12 12"><circle cx="6" cy="6" r="5.2" fill="none" stroke="#fff" stroke-width="1"/><ellipse cx="6" cy="6" rx="2.3" ry="5.2" fill="none" stroke="#fff" stroke-width="1"/><path d="M1 6h10M2 3.5h8M2 8.5h8" stroke="#fff" stroke-width=".8"/></svg>www.BrixImaging.com</p>
  <div class="company-name">BRIX<span>IMAGING</span></div>
</section>

<!-- Size 2 -->
<section class="ad ad--size2">
  <div class="hero-photo" role="img" aria-label="Black-and-white photo of a model with orange lips holding the VANT sensor beneath her chin"></div>
  <svg class="ad-shapes" viewBox="0 0 467 631" aria-hidden="true">
    <polygon fill="#ff6319" points="0,320 245,320 272,292 467,292 467,529 300,529 240,622 0,622"/>
    <path d="M198 229 L230 260" stroke="#2d3180" stroke-width="4" fill="none"/>
    <polygon fill="#2d3180" points="0,548 277,548 256,582 0,582"/>
  </svg>
  <h1 class="headline"><span class="headline__lead">A subscription</span><span class="headline__lead">option for</span><span class="headline__accent">intra-oral sensors</span><span class="headline__accent">is dumb.</span></h1>
  <p class="headline__aside">(until you do the math).</p>
  <div class="product-name">VANT</div>
  <p class="tagline">11 Million X-rays and Counting</p>
  <div class="social"><span class="social__dot"></span><span class="social__dot"></span><span class="social__dot"></span></div>
  <div class="price price--fee"><span class="price__amount">$1,999</span><span class="price__note">ONE-TIME<br>SIGN UP FEE</span></div>
  <div class="price price--monthly"><span class="price__amount">$139/mo</span><span class="price__note">CANCEL<br>ANYTIME</span></div>
  <div class="sensor-photo" role="img" aria-label="Product photo of the VANT intra-oral sensor with cable"></div>
  <ul class="benefits">
    <li class="benefits__item"><svg viewBox="0 0 10 10"><circle cx="5" cy="5" r="4.3" fill="none" stroke="#fff" stroke-width="1"/><path d="M3 5.2 L4.5 6.6 L7 3.8" fill="none" stroke="#fff" stroke-width="1"/></svg>Lifetime $0 deductible warranty</li>
    <li class="benefits__item"><svg viewBox="0 0 10 10"><circle cx="5" cy="5" r="4.3" fill="none" stroke="#fff" stroke-width="1"/><path d="M3 5.2 L4.5 6.6 L7 3.8" fill="none" stroke="#fff" stroke-width="1"/></svg>Unlimited support &amp; upgrades</li>
    <li class="benefits__item"><svg viewBox="0 0 10 10"><circle cx="5" cy="5" r="4.3" fill="none" stroke="#fff" stroke-width="1"/><path d="M3 5.2 L4.5 6.6 L7 3.8" fill="none" stroke="#fff" stroke-width="1"/></svg>Direct integration w/all major software</li>
    <li class="benefits__item"><svg viewBox="0 0 10 10"><circle cx="5" cy="5" r="4.3" fill="none" stroke="#fff" stroke-width="1"/><path d="M3 5.2 L4.5 6.6 L7 3.8" fill="none" stroke="#fff" stroke-width="1"/></svg>Affordable enough for every op</li>
    <li class="benefits__item"><svg viewBox="0 0 10 10"><circle cx="5" cy="5" r="4.3" fill="none" stroke="#fff" stroke-width="1"/><path d="M3 5.2 L4.5 6.6 L7 3.8" fill="none" stroke="#fff" stroke-width="1"/></svg>Preserve your capital</li>
  </ul>
  <p class="phone"><svg viewBox="0 0 24 24"><circle cx="12" cy="12" r="10.5" fill="none" stroke="#fff" stroke-width="1.8"/><path d="M8.3 6.5c.6-.4 1.3-.3 1.6.3l1 1.9c.3.5.1 1.1-.3 1.4l-.7.5c.5 1.4 1.5 2.6 2.9 3.3l.6-.6c.4-.4 1-.5 1.5-.2l1.8 1.1c.5.3.7 1 .3 1.5-.9 1.3-2.2 1.7-3.6 1.1-3-1.3-5.1-3.7-6-6.7-.4-1.4.1-2.8.9-3.6z" fill="#fff"/></svg>(555) 010-BRIX</p>
  <p class="website"><svg viewBox="0 0 12 12"><circle cx="6" cy="6" r="5.2" fill="none" stroke="#fff" stroke-width="1"/><ellipse cx="6" cy="6" rx="2.3" ry="5.2" fill="none" stroke="#fff" stroke-width="1"/><path d="M1 6h10M2 3.5h8M2 8.5h8" stroke="#fff" stroke-width=".8"/></svg>www.BrixImaging.com</p>
  <div class="company-name">BRIX<span>IMAGING</span></div>
</section>

<p class="size-label size-label--1">Size 1 -&nbsp; 8.25 x 10.75</p>
<p class="size-label size-label--2">Size 2 -&nbsp; 8.25 x 11.125</p>

</body>
</html>
```